New Facebook Banner

Hi
We are operating Ramen shop in Australia.(http://mizunokobowls.com)
I want to create new design for our Facebook banner and title is "Free Ramen on your Birthday".
Sample attached is our existing banner design. We would like to make it more modern and sophisticated.
We are so looking forward to seeing your design for our free ramen promotion.

https://www.facebook.com/mizunokobowls/

Industry/Entity Type

Japanese Restaurant

Font styles to use
Sans Serif

```html
<!DOCTYPE html>
<html lang="en">
<head>
<meta charset="utf-8">
<title>Free Ramen On Your Birthday – Facebook Banner</title>
<link rel="stylesheet" href="https://fonts.googleapis.com/css2?family=Kaushan+Script&family=Lato:ital,wght@0,700;1,400&display=swap">
<style>
  :root {
    --page-bg: #eeeeec;
    --orange-deep: #cf5a26;
    --orange-warm: #dc7a30;
    --gold: #e8b417;
    --rust: #b9652a;
    --wave-white: #ffffff;
    --wave-grey: #c9cacd;
    --text-light: #ffffff;
    --photo-red: #c8352c;
    --photo-noodle: #d99a4a;
    --photo-plate: #f4efe8;
    --bunting-a: #e1307e;
    --bunting-b: #6ab3e0;
    --bunting-c: #f2d534;
    --bunting-d: #4fae9c;
  }
  html, body {
    margin: 0;
    width: 1200px;
    height: 1200px;
    overflow: hidden;
    background: var(--page-bg);
  }
  .canvas {
    position: relative;
    width: 1200px;
    height: 1200px;
  }
  .facebook-banner {
    position: absolute;
    left: 30px;
    top: 389px;
    width: 1140px;
    height: 423px;
    display: block;
  }
  .promo-title {
    font-family: "Kaushan Script", cursive;
    font-size: 38px;
    fill: var(--text-light);
  }
  .web-label {
    font-family: "Lato", sans-serif;
    font-style: italic;
    font-size: 13px;
    fill: var(--text-light);
  }
  .web-address {
    font-family: "Lato", sans-serif;
    font-weight: 700;
    font-size: 15.5px;
    fill: var(--text-light);
  }
</style>
</head>
<body>
<main class="canvas">
  <svg class="facebook-banner" viewBox="0 0 852 316" preserveAspectRatio="none" xmlns="http://www.w3.org/2000/svg">
    <defs>
      <linearGradient id="photo-tones" x1="0" y1="0" x2="1" y2="0">
        <stop offset="0" stop-color="var(--photo-red)"/>
        <stop offset="0.2" stop-color="#d9a9a4"/>
        <stop offset="0.35" stop-color="var(--photo-noodle)"/>
        <stop offset="0.7" stop-color="#d8904a"/>
        <stop offset="0.88" stop-color="var(--photo-plate)"/>
        <stop offset="1" stop-color="#d77b7b"/>
      </linearGradient>
      <linearGradient id="accent-stripe" x1="0" y1="0" x2="1" y2="0">
        <stop offset="0" stop-color="var(--gold)"/>
        <stop offset="0.55" stop-color="#d99a2a"/>
        <stop offset="1" stop-color="var(--rust)"/>
      </linearGradient>
      <linearGradient id="orange-field" x1="0" y1="0" x2="1" y2="0">
        <stop offset="0" stop-color="var(--orange-deep)"/>
        <stop offset="1" stop-color="var(--orange-warm)"/>
      </linearGradient>
      <linearGradient id="bunting-tones" x1="0" y1="0" x2="1" y2="0">
        <stop offset="0" stop-color="var(--bunting-b)"/>
        <stop offset="0.25" stop-color="var(--bunting-d)"/>
        <stop offset="0.5" stop-color="var(--bunting-a)"/>
        <stop offset="0.75" stop-color="var(--bunting-c)"/>
        <stop offset="1" stop-color="var(--bunting-b)"/>
      </linearGradient>
    </defs>

    <rect class="food-photo" x="0" y="0" width="852" height="316" fill="url(#photo-tones)"
          role="img" aria-label="Photo of stir-fried ramen noodles with peppers on a plate over a checked cloth"/>

    <path class="accent-stripe" d="M0,198 C200,203 300,148 450,98 C600,48 750,38 852,30 L852,316 L0,316 Z" fill="url(#accent-stripe)"/>
    <path class="wave-white" d="M0,216 C200,218 300,166 450,116 C600,66 750,56 852,50 L852,316 L0,316 Z" fill="var(--wave-white)"/>
    <path class="wave-grey" d="M0,239 C200,234 350,194 500,154 C650,119 750,114 852,112 L852,316 L0,316 Z" fill="var(--wave-grey)"/>
    <path class="orange-field" d="M0,245 C200,240 350,200 500,160 C650,125 750,120 852,118 L852,316 L0,316 Z" fill="url(#orange-field)"/>

    <g class="bunting" role="img" aria-label="Festive string of coloured bunting flags">
      <polygon points="0,294 430,268 432,290 0,316" fill="url(#bunting-tones)" opacity="0.8"/>
      <polygon points="440,230 852,190 852,214 446,256" fill="url(#bunting-tones)" opacity="0.8"/>
    </g>

    <text class="promo-title" x="100" y="286" transform="rotate(-9.5 100 286)" textLength="665" lengthAdjust="spacingAndGlyphs">Free Ramen On Your Birthday!</text>

    <text class="web-label" x="615" y="271">Find out more at:</text>
    <text class="web-address" x="615" y="295">www.mizunokobowls.com</text>
  </svg>
</main>
</body>
</html>
```